Toward Bright Morrow (TWBM) Business Card - company with a mission

Note* The file attached... orange with "Toward Bright MORROW" (in CAPS) is our logo. I am also open to having the text "toward bright morrow" OUTSIDE the orange round logo for business card (so yes, you may take the text out).

The info: (the following info are separate. So either you can use Martin or Helena for now, but that will be 2 separate cards, not together in one card. Thanks!!

Martin K Pardo
202.555.0183
martin@towardbrightmorrow.example
Managing Partner

Helena R Voss
202.555.0147
helena@towardbrightmorrow.example
Managing Partner

Our website: www.towardbrightmorrow.example

TWBM LLC stands for Toward Bright Morrow (non profit arm is called dawn lift foundation)—our business is based out of New York City and has a non-profit arm where for every bar of soap you purchase, we donate a bar (don’t want any designs that limits us to only soap). Currently working with South Africa. We want the focus to be organic/natural soap with a mission.

Looking for a clean, fresh design.

Industry/Entity Type

Non-Profit

Requirements
Must have
• Clean, fresh, refreshing. Design should not be too busy.

```html
<!DOCTYPE html>
<html lang="en">
<head>
<meta charset="utf-8">
<title>Toward Bright Morrow – Business Card</title>
<link rel="stylesheet" href="https://fonts.googleapis.com/css2?family=Open+Sans:wght@400;600;700&display=swap">
<style>
  :root {
    --orange: #f4ae6c;
    --orange-soft: #f8c99b;
    --orange-text: #f29a4a;
    --paper: #eeeeee;
    --stripe: #d5d5d5;
    --charcoal: #2c2c2c;
    --ink: #1e1e1e;
    --white: #ffffff;
    --backdrop: #dcdad6;
  }
  * { margin: 0; padding: 0; box-sizing: border-box; }
  html, body {
    width: 1200px; height: 900px; overflow: hidden;
    background: var(--backdrop);
    font-family: "Open Sans", Arial, sans-serif;
  }
  .canvas { position: relative; width: 1200px; height: 900px; }

  .card {
    position: absolute; top: 100px;
    width: 400px; height: 700px;
    background: var(--paper);
    overflow: hidden;
    box-shadow: 0 6px 18px rgba(0,0,0,0.18);
  }
  .card--front { left: 150px; }
  .card--back  { left: 650px; }

  /* front */
  .side-stripe {
    position: absolute; left: 0; top: 0;
    width: 36px; height: 210px; background: var(--stripe);
  }
  .color-block {
    position: absolute; left: 36px; top: 0;
    width: 364px; height: 345px; background: var(--orange);
  }
  .name-bar {
    position: absolute; left: 0; top: 210px;
    width: 240px; height: 66px; background: var(--charcoal);
    color: var(--white); padding: 10px 0 0 18px;
  }
  .name-bar .person { font-size: 20px; font-weight: 700; line-height: 1.2; }
  .name-bar .role { font-size: 13px; font-weight: 700; line-height: 1.4; }

  .contact {
    position: absolute; left: 44px;
    display: flex; align-items: center; gap: 8px;
    font-size: 14px; color: var(--ink);
  }
  .contact--phone { top: 290px; }
  .contact--email { top: 316px; }
  .contact-icon {
    width: 18px; height: 18px; background: var(--orange-soft);
    display: flex; align-items: center; justify-content: center;
  }

  .seal {
    position: absolute;
    width: 236px; height: 236px; border-radius: 50%;
    background: var(--orange);
    box-shadow: 0 0 0 4px var(--white);
    display: flex; flex-direction: column; align-items: center; justify-content: center;
    color: var(--white); font-weight: 600; text-align: center;
    font-size: 30px; line-height: 1.1;
  }
  .card--front .seal { left: 140px; top: 362px; }
  .card--back .seal { left: 82px; top: 56px; }

  .web-row {
    position: absolute; left: 0; bottom: 24px; right: 16px;
    display: flex; align-items: flex-end; gap: 14px;
  }
  .web-tab { width: 70px; height: 36px; background: var(--orange); flex: none; }
  .web-address {
    font-size: 17px; color: var(--ink); letter-spacing: 0.2px;
    padding-bottom: 6px; white-space: nowrap;
  }
  .web-address b { color: var(--orange-text); font-weight: 700; }
</style>
</head>
<body>
<main class="canvas">

  <section class="card card--front" aria-label="Business card front">
    <div class="side-stripe"></div>
    <div class="color-block"></div>

    <div class="name-bar">
      <p class="person">Helena R Voss</p>
      <p class="role">Managing Partner</p>
    </div>

    <p class="contact contact--phone">
      <span class="contact-icon">
        <svg width="12" height="12" viewBox="0 0 24 24" aria-hidden="true">
          <path fill="#f29a4a" d="M6.6 10.8a15.1 15.1 0 0 0 6.6 6.6l2.2-2.2a1 1 0 0 1 1-.25 11.4 11.4 0 0 0 3.6.6 1 1 0 0 1 1 1V20a1 1 0 0 1-1 1A17 17 0 0 1 3 4a1 1 0 0 1 1-1h3.5a1 1 0 0 1 1 1c0 1.25.2 2.45.6 3.6a1 1 0 0 1-.25 1z"/>
        </svg>
      </span>
      202.555.0147
    </p>
    <p class="contact contact--email">
      <span class="contact-icon">
        <svg width="12" height="12" viewBox="0 0 24 24" aria-hidden="true">
          <path fill="#f29a4a" d="M3 5h18a1 1 0 0 1 1 1v12a1 1 0 0 1-1 1H3a1 1 0 0 1-1-1V6a1 1 0 0 1 1-1zm9 7.2L20 7H4z"/>
        </svg>
      </span>
      helena@towardbrightmorrow.example
    </p>

    <div class="seal"><span>Toward</span><span>Bright</span><span>Morrow</span></div>

    <div class="web-row">
      <span class="web-tab"></span>
      <p class="web-address">www.<b>towardbrightmorrow</b>.example</p>
    </div>
  </section>

  <section class="card card--back" aria-label="Business card back">
    <div class="seal"><span>Toward</span><span>Bright</span><span>Morrow</span></div>
    <div class="web-row">
      <span class="web-tab"></span>
      <p class="web-address">www.<b>towardbrightmorrow</b>.example</p>
    </div>
  </section>

</main>
</body>
</html>
```